Flyer-Design für Autolackiererei
Hallo es muss nur noch die Richtige Telefonnumer rein , die bekomm ich esrt von Fernolux zu geschickt
Zielgruppe
Karosserie & Autolackiererei
Autohäuser , Privatkunden , Bussunterhemen , LKW Unterhemen , Versicherungen
Aufgabenstellung
Neueröffung Von Autolackiererei ab 01.03.2019 bitte ganz wichtig muss auf flayer drauf.
Unfallinstansetztung , Fahrzeuglackierung Jeglicher Art , Oldtimer Restauration , Fahrzeugaufbereitung , Achsvermessung ,Felgen Lackieren ,Hagelschaden ,
inspektionen alle Fahrzeug Fabrikaten, Vexa, Reifenservice
Hol und Bring service ,scheibenaustausch abwicklung mit versicherung ,
Smart Repair

```html
<!DOCTYPE html>
<html lang="de">
<head>
<meta charset="utf-8">
<title>Autolackiererei Brenner – Neueröffnung</title>
<link href="https://fonts.googleapis.com/css2?family=Montserrat:wght@400;500;700;800&display=swap" rel="stylesheet">
<style>
  :root {
    --bg: #d0d0d0;
    --paper: #ffffff;
    --ink: #0b0b0b;
    --blue: #1f9bd7;
    --grey: #9a9a9a;
    --grey-dark: #6d6d6d;
    --white: #ffffff;
  }
  * { margin: 0; padding: 0; box-sizing: border-box; }
  html, body { width: 1000px; height: 1200px; overflow: hidden; background: var(--bg); }
  body { position: relative; font-family: "Montserrat", Arial, sans-serif; color: var(--ink); }

  .flyer-side {
    position: absolute; left: 107px; width: 786px; height: 393px;
    background: var(--paper); overflow: hidden;
  }
  .flyer-front { top: 170px; }
  .flyer-back { top: 637px; }

  /* Front */
  .hero-photo {
    position: absolute; left: 196px; top: 0; width: 590px; height: 382px;
    background: radial-gradient(ellipse at 62% 52%, #e9e9e9 0%, #f4f4f4 38%, #ffffff 72%);
  }
  .opening-banner {
    position: absolute; left: 0; top: 41px; width: 350px; height: 57px;
    background: var(--ink); color: var(--white);
    font-weight: 800; font-size: 35px; letter-spacing: 0.5px;
    display: flex; align-items: center; padding-left: 31px;
  }
  .opening-date {
    position: absolute; left: 151px; top: 88px; width: 256px; height: 38px;
    background: var(--grey); color: var(--ink);
    font-weight: 800; font-size: 29px;
    display: flex; align-items: center; padding-left: 20px;
    transform: rotate(-3deg); transform-origin: left center;
  }
  .brand-mark {
    position: absolute; left: 90px; top: 155px; width: 200px; height: 200px;
    display: flex; flex-direction: column; align-items: center; justify-content: center;
  }
  .brand-ring { position: absolute; inset: 0; }
  .brand-name {
    position: relative; font-weight: 700; font-size: 19px; line-height: 1.25;
    color: var(--grey-dark); text-align: center;
  }
  .front-claim {
    position: absolute; right: 40px; top: 311px; text-align: right;
    font-weight: 700; font-size: 20px; line-height: 26px; letter-spacing: 0.3px;
  }
  .front-claim .claim-accent { color: var(--blue); }

  /* Back */
  .service-list { position: absolute; left: 29px; list-style: none; font-weight: 700; }
  .service-list li::before { content: "· "; }
  .services-main { top: 37px; color: var(--blue); font-size: 20px; line-height: 27px; letter-spacing: 0.2px; }
  .services-extra { top: 129px; color: var(--ink); font-size: 15px; line-height: 23.8px; letter-spacing: 0.4px; }
  .services-extra .service-note {
    display: block; margin: -5px 0 -2px 9px; font-size: 11px; line-height: 16px;
    color: var(--grey-dark);
  }
  .services-extra .service-note::before { content: ""; }

  .contact-panel {
    position: absolute; left: 525px; top: 0; width: 261px; height: 393px;
    background: var(--ink); color: var(--white); text-align: center;
  }
  .contact-brand {
    position: absolute; left: 50px; top: 40px; width: 164px; height: 164px;
    display: flex; align-items: center; justify-content: center;
  }
  .contact-brand .brand-name { color: #8a8a8a; font-size: 16px; }
  .contact-title {
    position: absolute; left: 0; right: 0; top: 221px;
    color: var(--blue); font-weight: 700; font-size: 13px; letter-spacing: 7px; padding-left: 7px;
  }
  .contact-details {
    position: absolute; left: 0; right: 0; top: 264px;
    font-style: normal; font-weight: 500; font-size: 12.5px; line-height: 23.8px;
  }
</style>
</head>
<body>

<section class="flyer-side flyer-front">
  <div class="hero-photo" role="img" aria-label="Foto: Miniaturfiguren von Lackierern, die ein weißes Modellauto bearbeiten"></div>
  <div class="opening-banner">NEUERÖFFNUNG</div>
  <div class="opening-date">ab 01.03.2019</div>
  <div class="brand-mark">
    <svg class="brand-ring" viewBox="0 0 200 200" aria-hidden="true">
      <circle cx="100" cy="100" r="94" fill="none" stroke="var(--blue)" stroke-width="6"/>
    </svg>
    <p class="brand-name">Autolackiererei<br>Brenner</p>
  </div>
  <p class="front-claim">AUTOLACKIEREREI<br><span class="claim-accent">MEISTERBETRIEB</span></p>
</section>

<section class="flyer-side flyer-back">
  <ul class="service-list services-main">
    <li>FAHRZEUGLACKIERUNG JEGLICHER ART</li>
    <li>FELGEN LACKIEREN</li>
    <li>OLDTIMER RESTAURATION</li>
  </ul>
  <ul class="service-list services-extra">
    <li>INSPEKTIONEN ALLER FAHRZEUG-FABRIKATEN | VEXA</li>
    <li>UNFALLINSTANSETZTUNG</li>
    <li>ACHSVERMESSUNG</li>
    <li>SCHEIBENAUSTAUSCH<span class="service-note">(ABWICKLUNG MIT DER VERSICHERUNG)</span></li>
    <li>REIFENSERVICE</li>
    <li>FAHRZEUGAUFBEREITUNG</li>
    <li>HAGELSCHADEN</li>
    <li>SMART REPAIR</li>
    <li>HOL- &amp; BRING-SERVICE</li>
  </ul>

  <aside class="contact-panel">
    <div class="contact-brand">
      <svg class="brand-ring" style="position:absolute;inset:0" viewBox="0 0 164 164" aria-hidden="true">
        <circle cx="82" cy="82" r="77" fill="none" stroke="var(--blue)" stroke-width="5"/>
      </svg>
      <p class="brand-name">Autolackiererei<br>Brenner</p>
    </div>
    <p class="contact-title">MEISTERBETRIEB</p>
    <address class="contact-details">
      Eine Straße 1,<br>
      12345 Stadt<br>
      +49(0)123 45 67 890<br>
      info@lackiererei-brenner.de
    </address>
  </aside>
</section>

</body>
</html>
```